Redesign Login page

I want to redesign my login page to bring my 2 products closer together. I am only looking to redesign one login page, not 2.

For the logo, please make it solid and it can be black or white if helpful. I can also fine tune the logo if you get it close.

Coding

Coded - Design and coding required

Number of Pages Required

1 page

```html
<!DOCTYPE html>
<html lang="en">
<head>
<meta charset="UTF-8">
<title>Corvane – Login</title>
<link href="https://fonts.googleapis.com/css2?family=Inter:wght@400;500;600;700;800&display=swap" rel="stylesheet">
<style>
  :root {
    --page-bg: #adadad;
    --header-bg: #f1f3f2;
    --panel-bg: #ffffff;
    --ink: #1f2222;
    --ink-soft: #555b5a;
    --muted: #7a8180;
    --field-border: #dde4e3;
    --field-fill: #f1f3f2;
    --brand: #3d5f5c;
    --logo: #4a4d4d;
  }
  * { box-sizing: border-box; margin: 0; padding: 0; }
  html, body { width: 1200px; height: 874px; overflow: hidden; }
  body {
    background: var(--page-bg);
    font-family: "Inter", sans-serif;
    color: var(--ink);
    position: relative;
  }
  .login-screen {
    position: absolute;
    left: 420px; top: 37px;
    width: 360px; height: 800px;
    background: var(--header-bg);
    border-radius: 40px;
    overflow: hidden;
  }
  .brand-mark {
    position: absolute;
    top: 76px; left: 0; width: 100%;
    display: flex; justify-content: center; align-items: center; gap: 8px;
    font-size: 36px; font-weight: 700; color: var(--logo);
    letter-spacing: -0.5px;
  }
  .brand-mark .brand-square {
    width: 22px; height: 22px; background: var(--logo);
  }
  .login-panel {
    position: absolute;
    left: 0; top: 202px;
    width: 100%; height: 598px;
    background: var(--panel-bg);
    border-top-left-radius: 90px 70px;
  }
  .login-title {
    position: absolute;
    top: 72px; width: 100%;
    text-align: center;
    font-size: 32px; font-weight: 700;
    letter-spacing: -0.3px;
  }
  .field {
    position: absolute;
    left: 19px; width: 319px; height: 47px;
    border: 1px solid var(--field-border);
    border-radius: 6px;
    padding: 8px 13px 0;
  }
  .field-user { top: 139px; background: var(--panel-bg); }
  .field-password { top: 203px; background: var(--field-fill); }
  .field-label { font-size: 11.5px; color: var(--muted); line-height: 14px; }
  .field-value { font-size: 14px; color: var(--ink); line-height: 20px; margin-top: 1px; }
  .field-password .field-value { font-size: 12px; letter-spacing: 1px; line-height: 14px; }
  .field-icon { position: absolute; right: 14px; top: 50%; transform: translateY(-50%); }
  .btn-continue {
    position: absolute;
    left: 19px; top: 266px;
    width: 319px; height: 47px;
    background: var(--brand);
    border: none; border-radius: 6px;
    color: #fff;
    font: 600 16px "Inter", sans-serif;
  }
  .options-row {
    position: absolute;
    left: 34px; right: 34px; top: 327px;
    display: flex; justify-content: space-between; align-items: center;
    font-size: 13px;
  }
  .remember { display: flex; align-items: center; gap: 7px; color: var(--ink-soft); }
  .checkbox {
    width: 11px; height: 11px; background: var(--brand); border-radius: 1.5px;
    display: flex; align-items: center; justify-content: center;
  }
  .link { color: var(--brand); text-decoration: underline; text-underline-offset: 2px; }
  .alt-title {
    position: absolute; top: 389px; width: 100%;
    text-align: center; font-size: 13px; color: var(--ink-soft);
  }
  .alt-title strong { font-weight: 600; color: var(--ink); }
  .social-row {
    position: absolute; top: 420px; left: 59px;
    display: flex; gap: 25px;
  }
  .social-btn {
    width: 41px; height: 32px;
    border: 1px solid #d7dbdb; background: #fff;
    display: flex; align-items: center; justify-content: center;
    font-size: 8.5px; font-weight: 600; color: var(--ink-soft);
  }
  .signup-line {
    position: absolute; top: 504px; width: 100%;
    text-align: center; font-size: 13.5px; color: var(--ink);
  }
  .signup-line .link { font-weight: 600; margin-left: 3px; }
</style>
</head>
<body>
  <main class="login-screen">
    <div class="brand-mark"><span class="brand-square"></span>Corvane</div>

    <section class="login-panel">
      <h1 class="login-title">Login</h1>

      <div class="field field-user">
        <div class="field-label">User ID</div>
        <div class="field-value">customer@mailbox.com</div>
        <svg class="field-icon" width="14" height="9" viewBox="0 0 14 9" aria-hidden="true">
          <path d="M1.5 1.5 L7 7 L12.5 1.5" fill="none" stroke="#2a2e2e" stroke-width="2" stroke-linecap="round" stroke-linejoin="round"/>
        </svg>
      </div>

      <div class="field field-password">
        <div class="field-label">Password</div>
        <div class="field-value">••••••••</div>
        <svg class="field-icon" width="19" height="16" viewBox="0 0 19 16" aria-hidden="true">
          <path d="M1.5 8 C4 3.5 15 3.5 17.5 8 C15 12.5 4 12.5 1.5 8 Z" fill="none" stroke="#2a2e2e" stroke-width="1.5"/>
          <circle cx="9.5" cy="8" r="2.4" fill="none" stroke="#2a2e2e" stroke-width="1.5"/>
          <line x1="3" y1="1.5" x2="16" y2="14.5" stroke="#2a2e2e" stroke-width="1.5" stroke-linecap="round"/>
        </svg>
      </div>

      <button class="btn-continue" type="button">Continue</button>

      <div class="options-row">
        <label class="remember">
          <span class="checkbox">
            <svg width="8" height="7" viewBox="0 0 8 7" aria-hidden="true"><path d="M1 3.5 L3 5.5 L7 1" fill="none" stroke="#fff" stroke-width="1.4"/></svg>
          </span>
          Remember Me
        </label>
        <span class="link">Forgot password?</span>
      </div>

      <p class="alt-title"><strong>Or</strong> Sign in with</p>

      <div class="social-row">
        <span class="social-btn">Gleam</span>
        <span class="social-btn">Facet</span>
        <span class="social-btn">Orchard</span>
        <span class="social-btn">Chirp</span>
      </div>

      <p class="signup-line">Don’t have an account? <span class="link">Sign Up</span></p>
    </section>
  </main>
</body>
</html>
```